Business Card Design

I need a business card design. I am a sole practitioner.I am a psychotherapist and I need a professional card. I am also an art therapist (a form of psychotherapy using art) so I want the image to be professional/creative/maybe ethnic. I do not want a boring minimalist "medical" image, nor do I want it too hippy/tree hugging.
Colours like reds/ochres/yellows would be good.
Contact Information for Business Card
Mira Hask
Psychotherapy, Counselling and Art Therapy
Wunnara Lodge Counselling and Wellbeing services
17 Pellow Road, Toowong 4066
0417639052 www.MiraHask.com.au
on rear of card I need the option to have at least 4 or 5 appointment times /dates

```html
<!DOCTYPE html>
<html lang="en">
<head>
<meta charset="utf-8">
<title>Mira Hask – Business Card</title>
<link rel="stylesheet" href="https://fonts.googleapis.com/css2?family=Lobster&family=Ubuntu:wght@500;700&family=Roboto+Condensed:wght@400;700&display=swap">
<style>
  :root {
    --backdrop: #3b3b3d;
    --card: #e9bb6c;
    --ink: #1b1611;
    --frame: #8a6530;
    --art-dark: #15110c;
    --art-gold: #b08a45;
  }
  * { box-sizing: border-box; margin: 0; padding: 0; }
  html, body {
    width: 1200px; height: 770px; overflow: hidden;
    background: var(--backdrop);
  }
  .canvas {
    position: relative; width: 1200px; height: 770px;
    display: flex; align-items: center; justify-content: center;
  }
  .card {
    position: relative; width: 1000px; height: 611px;
    background: var(--card); color: var(--ink);
    box-shadow: 0 6px 18px rgba(0,0,0,.35);
  }
  .artwork {
    position: absolute; left: 78px; top: 128px;
    width: 380px; height: 360px;
    background: var(--frame); padding: 16px;
  }
  .artwork-fill {
    width: 100%; height: 100%;
    background: linear-gradient(135deg, var(--art-dark) 0%, #3a2a15 45%, var(--art-gold) 100%);
  }
  .details { position: absolute; left: 505px; top: 58px; right: 40px; }
  .name {
    font-family: "Lobster", cursive;
    font-size: 76px; font-weight: 400; line-height: 1;
    margin-left: 0;
  }
  .profession {
    font-family: "Ubuntu", sans-serif; font-weight: 700;
    font-size: 33px; line-height: 1.25; margin-top: 34px;
  }
  .practice {
    font-family: "Roboto Condensed", sans-serif; font-weight: 700;
    font-size: 26px; line-height: 1.25; margin-top: 30px;
  }
  .contact {
    list-style: none; margin-top: 52px;
    font-family: "Roboto Condensed", sans-serif; font-weight: 400;
    font-size: 25px; line-height: 1.4;
  }
  .contact li { display: flex; align-items: center; gap: 14px; }
  .contact svg { width: 20px; height: 20px; fill: var(--ink); flex: none; }
</style>
</head>
<body>
<div class="canvas">
  <section class="card">
    <div class="artwork">
      <div class="artwork-fill" role="img" aria-label="Decorative black and gold pattern of flowing vertical bands and spirals"></div>
    </div>
    <div class="details">
      <h1 class="name">Mira Hask</h1>
      <p class="profession">Psychotherapy<br>and Counselling</p>
      <p class="practice">Wunnara Lodge Counselling &amp;<br>Wellbeing Services</p>
      <ul class="contact">
        <li>
          <svg viewBox="0 0 24 24" aria-hidden="true"><path d="M3 8c0-3 4-4 9-4s9 1 9 4v2h-5V8c-1-.6-2.5-1-4-1s-3 .4-4 1v2H3zM6 12h12l2 8H4z"/></svg>
          <span>0417 639052</span>
        </li>
        <li>
          <svg viewBox="0 0 24 24" aria-hidden="true"><path d="M12 2a7 7 0 0 0-7 7c0 5 7 13 7 13s7-8 7-13a7 7 0 0 0-7-7zm0 9.5A2.5 2.5 0 1 1 12 6.5a2.5 2.5 0 0 1 0 5z"/></svg>
          <span>17 Pellow Road, Toowong, 4066</span>
        </li>
        <li>
          <svg viewBox="0 0 24 24" aria-hidden="true"><path d="M12 2a10 10 0 1 0 0 20 10 10 0 0 0 0-20zm6.9 9h-3a15 15 0 0 0-1.3-5.6A8 8 0 0 1 18.9 11zM12 4.1c.9 1.2 1.8 3.6 2 6.9h-4c.2-3.3 1.1-5.7 2-6.9zM9.4 5.4A15 15 0 0 0 8.1 11h-3a8 8 0 0 1 4.3-5.6zM5.1 13h3a15 15 0 0 0 1.3 5.6A8 8 0 0 1 5.1 13zm6.9 6.9c-.9-1.2-1.8-3.6-2-6.9h4c-.2 3.3-1.1 5.7-2 6.9zm2.6-1.3a15 15 0 0 0 1.3-5.6h3a8 8 0 0 1-4.3 5.6z"/></svg>
          <span>www.MiraHask.com.au</span>
        </li>
      </ul>
    </div>
  </section>
</div>
</body>
</html>
```